ultra-minimalist business card

front (black background, matte):

tarik b. hosseny
writer | photographer
get@tarikhosseny.com

back (white background, matte):

a picture speaks a thousand words;
a word draws a thousand pictures.

www.tarikhosseny.com

all text should be small (white or silver - as long as it shows against the black - on the front; black or gray - as long as it shows against the white - on the back).

feel free to get creative in terms of arrangement, alignment, and font type, but remember, the overall style is minimalist, so nothing too fancy, please.

thanks.

```html
<!DOCTYPE html>
<html lang="en">
<head>
<meta charset="utf-8">
<title>Tarik B. Hosseny — Business Card</title>
<link rel="stylesheet" href="https://fonts.googleapis.com/css2?family=Kaushan+Script&family=Montserrat:wght@400;500&display=swap">
<style>
  :root {
    --backdrop: #d6d6d6;
    --card-black: #0c0c0c;
    --card-white: #ffffff;
    --ink-white: #ffffff;
    --ink-black: #141414;
    --ink-faint: #ececec;
    --script: "Kaushan Script", cursive;
    --sans: "Montserrat", sans-serif;
  }
  * { box-sizing: border-box; margin: 0; padding: 0; }
  html, body {
    width: 1200px;
    height: 1200px;
    overflow: hidden;
    background: var(--backdrop);
  }
  .canvas {
    position: relative;
    width: 1200px;
    height: 1200px;
  }
  .card {
    position: absolute;
    left: 250px;
    width: 700px;
    height: 400px;
    overflow: hidden;
    box-shadow: 0 18px 40px rgba(0, 0, 0, 0.18);
  }
  .card--front {
    top: 150px;
    background: var(--card-black);
    color: var(--ink-white);
    display: flex;
    flex-direction: column;
    align-items: center;
    justify-content: center;
    text-align: center;
  }
  .card--back {
    top: 640px;
    background: var(--card-white);
    color: var(--ink-black);
  }
  .name {
    font-family: var(--script);
    font-size: 62px;
    font-weight: 400;
    line-height: 1.1;
    letter-spacing: 1px;
  }
  .role {
    margin-top: 22px;
    font-family: var(--sans);
    font-size: 15px;
    font-weight: 500;
    letter-spacing: 6px;
    text-transform: uppercase;
  }
  .email {
    margin-top: 18px;
    font-family: var(--sans);
    font-size: 15px;
    font-weight: 400;
    letter-spacing: 5px;
    text-transform: uppercase;
  }
  .watermark {
    position: absolute;
    left: 30px;
    top: 20px;
    font-family: var(--script);
    font-size: 150px;
    line-height: 0.95;
    color: var(--ink-faint);
    white-space: nowrap;
  }
  .back-content {
    position: absolute;
    inset: 0;
    display: flex;
    flex-direction: column;
    align-items: center;
    justify-content: center;
    text-align: center;
  }
  .quote {
    font-family: var(--sans);
    font-size: 15px;
    font-weight: 500;
    letter-spacing: 3px;
    line-height: 1.6;
    text-transform: uppercase;
  }
  .website {
    margin-top: 26px;
    font-family: var(--sans);
    font-size: 15px;
    font-weight: 500;
    letter-spacing: 6px;
    text-transform: uppercase;
  }
</style>
</head>
<body>
  <main class="canvas">
    <section class="card card--front" aria-label="Card front">
      <h1 class="name">Tarik B. Hosseny</h1>
      <p class="role">Writer | Photographer</p>
      <p class="email">get@tarikhosseny.com</p>
    </section>

    <section class="card card--back" aria-label="Card back">
      <div class="watermark" aria-hidden="true">Tarik B.<br>Hosseny</div>
      <div class="back-content">
        <p class="quote">A picture speaks a thousand words;<br>a word draws a thousand pictures.</p>
        <p class="website">www.tarikhosseny.com</p>
      </div>
    </section>
  </main>
</body>
</html>
```